Varrick Development and Management Corp Stationery Design Project

Based on the logo, a stationary format that can be used for correspondence with all project stakeholders. Typically this involves landowners, public officials, general public, and investors. It needs to be clean and professional, representing the two engineers that manage the company.
Updates

Target Market(s)

Public officials, investors, project stakeholders, and landowners. All or english speaking, residing in North America. Company is based in Calgary, Alberta, Canada. Project values range fro $10MM to $500MM CAD.

Industry/Entity Type

It Company

Requirements
Should not have
• No references to tropics, palm trees, or similar beaches.

```html
<!DOCTYPE html>
<html lang="en">
<head>
<meta charset="utf-8">
<title>Varrick Development and Management Corp – Business Card</title>
<link rel="stylesheet" href="https://fonts.googleapis.com/css2?family=Didact+Gothic&display=swap">
<style>
  :root {
    --stage: #e9e9ee;
    --charcoal: #3a3a3e;
    --lime: #9cb51e;
    --slate: #767d86;
    --ink: #55585d;
    --paper: #f7f8fa;
    --font: "Didact Gothic", "Century Gothic", sans-serif;
  }
  * { box-sizing: border-box; margin: 0; padding: 0; }
  html, body { width: 1200px; height: 934px; overflow: hidden; }
  body {
    background: var(--stage);
    font-family: var(--font);
    position: relative;
  }
  .card {
    position: absolute;
    top: 317px;
    width: 520px;
    height: 300px;
    overflow: hidden;
    box-shadow: 0 6px 18px rgba(0,0,0,0.12);
  }
  .card--back { left: 60px; background: var(--charcoal); }
  .card--front { left: 620px; background: var(--paper); }

  .brand { position: absolute; display: flex; flex-direction: column; }
  .brand__row { display: flex; align-items: center; gap: 10px; }
  .brand__square { width: 14px; height: 14px; background: var(--lime); }
  .brand__name {
    color: var(--lime);
    font-size: 40px;
    letter-spacing: 2px;
    line-height: 1;
  }
  .brand__tagline {
    font-size: 11.5px;
    margin-top: 6px;
    margin-left: 24px;
  }
  .card--back .brand { left: 44px; top: 48px; }
  .card--back .brand__tagline { color: #9a9da3; }
  .card--front .brand { left: 40px; top: 110px; }
  .card--front .brand__tagline { color: var(--ink); }

  .back__stripe {
    position: absolute; left: 0; right: 0; bottom: 0;
    height: 5px; background: var(--lime);
  }

  .person { position: absolute; right: 40px; top: 36px; text-align: left; }
  .person__name { color: var(--lime); font-size: 17px; letter-spacing: 1px; }
  .person__role { color: var(--ink); font-size: 12.5px; margin-top: 2px; }

  .contact {
    position: absolute; left: 40px; bottom: 40px;
    font-size: 12px; color: var(--ink); line-height: 1.6;
  }
  .contact__label { color: var(--lime); }

  .band { position: absolute; height: 13px; }
  .band--slate { left: 0; width: 80%; bottom: 14px; background: var(--slate); }
  .band--lime { left: calc(80% + 3px); right: 0; bottom: 14px; background: var(--lime); }
</style>
</head>
<body>
  <section class="card card--back" aria-label="Card back">
    <div class="brand">
      <div class="brand__row">
        <span class="brand__square"></span>
        <span class="brand__name">VARRICK</span>
      </div>
      <span class="brand__tagline">Development and Management Corp</span>
    </div>
    <div class="back__stripe"></div>
  </section>

  <section class="card card--front" aria-label="Card front">
    <div class="person">
      <p class="person__name">NOLAN PIERCE</p>
      <p class="person__role">Managing Director</p>
    </div>
    <div class="brand">
      <div class="brand__row">
        <span class="brand__square"></span>
        <span class="brand__name">VARRICK</span>
      </div>
      <span class="brand__tagline">Development and Management Corp</span>
    </div>
    <div class="contact">
      <p>P.O.Box 480117 Calgary, AB · <span class="contact__label">Tel:</span> +1 403 555 0142</p>
      <p><span class="contact__label">E-mail:</span> info@varrick.com · www.varrick.com</p>
    </div>
    <div class="band band--slate"></div>
    <div class="band band--lime"></div>
  </section>
</body>
</html>
```